Medical practice in the United States needs a landing page

Our medical practice, based in Dallas, Texas, is called 'Talwick Headache Clinics.' We perform the Talwick Method on patients to treat chronic, severe head pain.

We currently have a landing page for our Chatterly ads, but we'd like to improve the page's design to increase the lead conversion rate. The landing page contains a form that allows people to register for our free, on-demand informational webinar about the procedure. Either part of the registration form or all of the registration form must be above the fold.

Here is the link to the landing page that needs a more attractive design: https://talwickheadache.example/migraine-treatment-webinars/talwick-treatment-free-patient-webinar/

Once a lead submits the registration form on that page, they are redirected to a different page on the site that contains the webinar video.

Here is a direct link to the page that contains the actual video (note: this is NOT the page for which I am requesting an improved design for this project; I am only including this link so that you can watch the video if you think it will help you create a design for the other page):

https://talwickheadache.example/talwick-headache-clinics-patient-information-webinar/
Updates

Designs look the same

Hello all,

The designs so far have been very impressive! Thank you all for your hard work. Please don't feel compelled to use my exact wording, though, for the description of the webinar. The only requirement is that the form on the page be present and contain the same form fields.

Thanks again!

Target Market(s)

Patients with chronic, severe head pain

Industry/Entity Type

Healthcare

Requirements
Must have
• Either part of the registration form or all of the registration form must be above the fold.
Should not have
• The registration form located completely below the fold.

```html
<!DOCTYPE html>
<html lang="en">
<head>
<meta charset="utf-8">
<title>Talwick Method – Free Patient Webinar</title>
<link href="https://fonts.googleapis.com/css2?family=Poppins:ital,wght@0,300;0,400;0,500;0,600;1,400&display=swap" rel="stylesheet">
<style>
:root{
  --teal:#1f5e73;
  --green:#8cc462;
  --green-soft:#c9eab0;
  --green-title:#a6d06e;
  --navy:#27313f;
  --text:#5d6470;
  --muted:#9aa0a8;
  --field:#f0f0f3;
  --hero:#eff9fb;
  --band:#e3f3f7;
  --line:#e3e5e8;
  --white:#fff;
}
*{box-sizing:border-box;margin:0;padding:0}
html,body{width:1200px;height:3405px;overflow:hidden}
body{position:relative;font-family:'Poppins',sans-serif;color:var(--navy);background:var(--white)}
.abs{position:absolute}
/* header */
.site-header{left:0;top:0;width:1200px;height:99px;background:var(--white);box-shadow:0 2px 10px rgba(0,0,0,.05);z-index:3}
.brand{font-size:19px;font-weight:600;color:var(--navy);white-space:nowrap}
.site-header .brand{left:91px;top:36px}
.nav{left:390px;top:42px;display:flex;font-size:10.5px;color:var(--text)}
.nav span{padding:0 15px;border-left:1px solid #c7cbd0;line-height:12px}
.nav span:first-child{border:none;padding-left:0;color:var(--teal);font-weight:600}
.btn{background:var(--teal);color:var(--white);font-weight:600;display:flex;align-items:center;justify-content:center;border-radius:3px}
.header-btn{left:983px;top:33px;width:125px;height:32px;font-size:10.5px}
/* hero */
.hero{left:0;top:99px;width:1200px;height:540px;background:var(--hero);overflow:hidden}
.hero svg{position:absolute;left:0;top:0}
.hero-title{left:0;width:1200px;text-align:center;top:138px;font-size:31px;font-weight:600;color:var(--green-title)}
.hero-sub{left:0;width:1200px;text-align:center;top:188px;font-size:31px;font-weight:600;color:var(--navy)}
.form-card{left:258px;top:260px;width:684px;height:518px;background:var(--white);box-shadow:0 4px 20px rgba(0,0,0,.08);border-bottom:4px solid var(--teal)}
.form-title{left:0;width:684px;top:40px;text-align:center;font-size:19px;font-weight:500}
.field{background:var(--field);height:38px;width:220px;font-size:9.5px;color:var(--muted);padding:13px 26px}
.check{left:101px;top:375px;display:flex;align-items:center;font-size:9.5px;font-weight:500;gap:6px}
.check i{width:12px;height:12px;border:1px solid #aaa;display:block}
.note{left:101px;top:403px;width:460px;font-size:9.5px;font-style:italic;color:var(--muted);line-height:17px}
.note u{text-decoration:underline}
.form-btn{left:214px;top:481px;width:255px;height:35px;font-size:10px;border-radius:0}
/* headings */
.section-title{left:0;width:1200px;text-align:center;font-size:26px;font-weight:600}
/* topics */
.topic{width:320px;height:220px;border:1px solid #dadde1;box-shadow:0 2px 6px rgba(0,0,0,.04);background:var(--white)}
.icon{left:33px;top:32px;width:51px;height:51px;background:var(--green-soft);border-radius:3px;display:flex;align-items:center;justify-content:center}
.topic h3{position:absolute;left:33px;top:98px;font-size:16px;font-weight:600}
.topic p{position:absolute;left:33px;top:130px;width:270px;font-size:10px;line-height:18px;color:var(--text)}
/* offer */
.photo{border-radius:2px}
.offer-title{width:312px;text-align:center;font-size:16.5px;font-weight:500}
.offer-text{width:312px;text-align:center;font-size:10px;line-height:17px;color:var(--text)}
.arrow-btn{width:33px;height:33px;border-radius:5px;background:var(--green);display:flex;align-items:center;justify-content:center}
/* why */
.why-badge{left:436px;top:2090px;width:271px;height:105px;background:var(--navy);border-radius:30px 0 30px 0;box-shadow:6px 6px 0 rgba(255,255,255,.9),8px 8px 14px rgba(0,0,0,.12);color:var(--white);font-size:20px;font-weight:500;line-height:30px;padding:22px 38px}
.why-item{left:730px;width:380px}
.why-item h4{display:flex;align-items:center;gap:12px;font-size:12.5px;font-weight:600;color:var(--teal)}
.why-item h4 i{width:19px;height:19px;border:1.5px solid var(--green);border-radius:4px;display:flex;align-items:center;justify-content:center}
.why-item p{margin:13px 0 0 30px;font-size:10px;line-height:18px;color:var(--text)}
.why-item u{color:var(--text)}
/* testimonials */
.reviews{left:0;top:2395px;width:1200px;height:388px;background:var(--band);overflow:hidden}
.reviews h2{position:absolute;left:91px;top:40px;font-size:25px;font-weight:600}
.nav-arrow{top:39px;width:37px;height:37px;border-radius:6px;display:flex;align-items:center;justify-content:center}
.card{top:132px;width:400px;height:194px;background:var(--white);border-radius:8px;box-shadow:0 3px 12px rgba(0,0,0,.06)}
.avatar{left:38px;top:-20px;width:50px;height:50px;border-radius:50%;border:3px solid var(--white);background:linear-gradient(#9aa4ad,#5f6a74)}
.card p{position:absolute;left:45px;top:50px;width:320px;font-size:10px;line-height:19px;color:var(--text)}
.card h5{position:absolute;left:45px;top:128px;font-size:16.5px;font-weight:600}
.card small{position:absolute;left:45px;top:152px;font-size:9px;color:var(--muted)}
.stars{position:absolute;left:282px;top:130px;color:#f5a623;font-size:14px;letter-spacing:2px}
/* cta */
.cta{left:91px;top:2824px;width:1017px;height:243px;background:var(--green-title);overflow:hidden;text-align:center;color:var(--white)}
.cta svg{position:absolute;left:0;top:0}
.cta h2{position:relative;margin-top:46px;font-size:35px;font-weight:600}
.cta p{position:relative;margin-top:12px;font-size:11px;line-height:20px}
.cta-btn{left:436px;top:173px;width:146px;height:32px;font-size:10px}
/* footer */
.footer-line{left:0;top:3112px;width:1200px;height:1px;background:var(--line)}
.site-footer .brand{left:91px;top:3162px}
.footer-about{left:91px;top:3205px;width:225px;font-size:10px;line-height:17px;color:var(--text)}
.socials{left:91px;top:3282px;display:flex;gap:6px}
.socials i{display:block;width:26px;height:26px;border-radius:50%;background:var(--teal)}
.fcol{top:3168px;font-size:10px;color:var(--text)}
.fcol h6{font-size:11px;font-weight:600;color:var(--navy);margin-bottom:17px}
.fcol div{margin-bottom:14px}
.bottom-bar{left:0;top:3362px;width:1200px;height:43px;background:#2b2f36;color:#b3b7bd;font-size:10px}
</style>
</head>
<body>

<header class="site-header abs">
  <div class="brand abs">Talwick Headache Clinics</div>
  <nav class="nav abs"><span>Talwick Method®</span><span>About</span><span>Research</span><span>Reviews</span><span>FAQ</span><span>Ask Our Patients</span><span>Free Webinar</span></nav>
  <div class="btn header-btn abs">Contact Us</div>
</header>

<section class="hero abs">
  <svg width="1200" height="540"><polygon points="0,430 258,490 258,540 0,540" fill="#fff"/><polygon points="942,510 1200,420 1200,540 942,540" fill="#fff"/></svg>
</section>
<h1 class="hero-title abs">The Talwick Method®</h1>
<h2 class="hero-sub abs">A Potentially Permanent Migraine Treatment</h2>

<form class="form-card abs">
  <div class="form-title abs">Webinar Registration Form</div>
  <div class="field abs" style="left:101px;top:102px">First Name *</div>
  <div class="field abs" style="left:356px;top:102px">Last Name *</div>
  <div class="field abs" style="left:101px;top:158px">Email Address</div>
  <div class="field abs" style="left:356px;top:158px">Phone Number *</div>
  <div class="field abs" style="left:101px;top:213px">Select Diagnosis *</div>
  <div class="field abs" style="left:356px;top:213px">Select Insurance Carrier *</div>
  <div class="field abs" style="left:101px;top:274px;width:475px;height:83px">Message *</div>
  <div class="check abs"><i></i>I agree with the site's User Agreement and Privacy Policy.</div>
  <div class="note abs">Please read the site's <u>Terms of Use</u> and <u>Privacy Policy</u>. Checking the box acknowledges that you have read, understand, and agree to the site's policies.</div>
  <div class="btn form-btn abs">SCHEDULE FREE WEBINAR</div>
</form>

<h2 class="section-title abs" style="top:826px">Webinar Topics</h2>

<div class="topic abs" style="left:91px;top:903px"><div class="icon abs"><svg width="24" height="24"><rect x="2" y="2" width="20" height="20" rx="2" fill="#1f5e73"/><rect x="7" y="11" width="2" height="7" fill="#c9eab0"/><rect x="11" y="8" width="2" height="10" fill="#c9eab0"/><rect x="15" y="13" width="2" height="5" fill="#c9eab0"/></svg></div><h3>The Numbers</h3><p>The procedure's compelling statistics: performed for over 25 years, more than 1000 patients, and a greater than 80%success rate!</p></div>
<div class="topic abs" style="left:440px;top:903px"><div class="icon abs"><svg width="26" height="24"><polygon points="5,3 21,3 25,9 13,22 1,9" fill="#1f5e73"/><path d="M1 9H25M9 3 7 9 13 22 19 9 17 3" stroke="#c9eab0" stroke-width="1.2" fill="none"/></svg></div><h3>The Benefits</h3><p>Ability to test the stimulator to make sure it works for you. Medication-free migraine pain relief. Effectively treats intractable migraines.</p></div>
<div class="topic abs" style="left:789px;top:903px"><div class="icon abs"><svg width="26" height="26"><circle cx="13" cy="13" r="12" fill="#1f5e73"/><path d="M9.5 10a3.5 3.5 0 1 1 5 3c-1.3.6-1.5 1.3-1.5 2.5" stroke="#c9eab0" stroke-width="2.2" fill="none"/><circle cx="13" cy="19.5" r="1.4" fill="#c9eab0"/></svg></div><h3 style="top:104px">The Answer to FAQ</h3><p style="top:135px">How does the Talwick Method® work? Am I a candidate for the procedure? Is the procedure safe? And more!</p></div>

<div class="topic abs" style="left:91px;top:1152px"><div class="icon abs"><svg width="22" height="26"><path d="M2 2h12l6 6v16H2z" fill="#1f5e73"/><polygon points="8,11 15,15 8,19" fill="#c9eab0"/></svg></div><h3 style="left:30px">The Media</h3><p>Video clips of the Talwick Method featured on Health Hour, Channel 9 News, and Metro News.</p></div>
<div class="topic abs" style="left:440px;top:1152px"><div class="icon abs"><svg width="22" height="26"><rect x="2" y="4" width="18" height="21" rx="2" fill="#1f5e73"/><rect x="7" y="1" width="8" height="6" rx="1.5" fill="#1f5e73" stroke="#c9eab0"/><rect x="6" y="12" width="10" height="2" fill="#c9eab0"/><rect x="6" y="17" width="10" height="2" fill="#c9eab0"/></svg></div><h3>The Treatment Process</h3><p>Details about the free initial consultation. The trial procedure vs. the permanent procedure. The treatment steps and timetable.</p></div>
<div class="topic abs" style="left:789px;top:1152px"><div class="icon abs"><svg width="24" height="24"><polygon points="12,1 15,9 23,9 17,14 19,22 12,17 5,22 7,14 1,9 9,9" fill="#1f5e73"/></svg></div><h3>The Patient Stories</h3><p>Many of our patients describe how the procedure changed their lives. Information about our patient ambassador program.</p></div>

<h2 class="section-title abs" style="top:1426px">What We Offer</h2>

<div class="photo abs" role="img" aria-label="Presenter recording a webinar at a desk with monitors and a microphone" style="left:91px;top:1509px;width:312px;height:230px;background:linear-gradient(135deg,#eef1f2,#c9d0d3 60%,#3b3f42)"></div>
<div class="photo abs" role="img" aria-label="Medical specialist in mask and gloves in a treatment room" style="left:443px;top:1509px;width:312px;height:230px;background:linear-gradient(135deg,#6f7779,#d9dcdc 50%,#8a9092)"></div>
<div class="photo abs" role="img" aria-label="Woman holding her head in pain" style="left:798px;top:1509px;width:312px;height:230px;background:linear-gradient(135deg,#3e4a47,#9c8a80 55%,#4e5a58)"></div>

<div class="offer-title abs" style="left:91px;top:1764px">Free Webinar</div>
<div class="offer-title abs" style="left:443px;top:1764px">Migraine Treatment</div>
<div class="offer-title abs" style="left:798px;top:1764px">Headache Help</div>
<div class="offer-text abs" style="left:91px;top:1800px">The procedure's compelling statistics: performed for over 25 years, &nbsp;performed for over 25 years, more than</div>
<div class="offer-text abs" style="left:443px;top:1800px">The procedure's compelling statistics: performed for over 25 years, &nbsp;performed for over 25 years, more than</div>
<div class="offer-text abs" style="left:798px;top:1800px">The procedure's compelling statistics: performed for over 25 years, &nbsp;performed for over 25 years, more than</div>
<div class="arrow-btn abs" style="left:231px;top:1857px"><svg width="10" height="12"><path d="M3 2l4 4-4 4" stroke="#27313f" stroke-width="1.6" fill="none"/></svg></div>
<div class="arrow-btn abs" style="left:582px;top:1857px"><svg width="10" height="12"><path d="M3 2l4 4-4 4" stroke="#27313f" stroke-width="1.6" fill="none"/></svg></div>
<div class="arrow-btn abs" style="left:937px;top:1857px"><svg width="10" height="12"><path d="M3 2l4 4-4 4" stroke="#27313f" stroke-width="1.6" fill="none"/></svg></div>

<div class="photo abs" role="img" aria-label="Doctor in a white coat holding a stethoscope" style="left:91px;top:1957px;width:471px;height:369px;background:linear-gradient(120deg,#e6edf4,#cfdbe6 55%,#f2f5f8)"></div>
<div class="why-badge abs">Why Talwick Headache Clinics?</div>

<h2 class="abs" style="left:730px;top:1953px;font-size:24px;font-weight:600">Why Us?</h2>
<div class="why-item abs" style="top:2021px"><h4><i><svg width="8" height="10"><path d="M2 1l4 4-4 4" stroke="#8cc462" stroke-width="1.4" fill="none"/></svg></i>Documented Proven Success</h4><p>The procedure's compelling statistics: performed for over 25 years, more than 1000 patients, and a greater than 80%success rate!</p></div>
<div class="why-item abs" style="top:2126px"><h4><i><svg width="8" height="10"><path d="M2 1l4 4-4 4" stroke="#8cc462" stroke-width="1.4" fill="none"/></svg></i>World's Most Experienced</h4><p>Talwick Headache specialists have been performing the Talwick Method since they invented it in 1992.</p></div>
<div class="why-item abs" style="top:2231px"><h4><i><svg width="8" height="10"><path d="M2 1l4 4-4 4" stroke="#8cc462" stroke-width="1.4" fill="none"/></svg></i>Research Partnerships</h4><p>Partnered with <u>Halvern Clinic</u> and other leading institutions to bring the latest technology and discoveries.</p></div>

<section class="reviews abs">
  <h2>What Our Customers Say</h2>
  <div class="nav-arrow abs" style="left:1016px;border:1.5px solid #27313f"><svg width="10" height="12"><path d="M7 2 3 6l4 4" stroke="#27313f" stroke-width="1.6" fill="none"/></svg></div>
  <div class="nav-arrow abs" style="left:1072px;background:#27313f"><svg width="10" height="12"><path d="M3 2l4 4-4 4" stroke="#fff" stroke-width="1.6" fill="none"/></svg></div>
  <div class="card abs" style="left:91px"><div class="avatar abs" role="img" aria-label="Reviewer portrait"></div><p>Can hardly wait. Had my trial last month, permanent 8/31. Works amazing. I have had migraines for over 50 years and tried so many things.”</p><h5>Bonnie</h5><small>Two weeks ago</small><div class="stars">★★★★★</div></div>
  <div class="card abs" style="left:542px"><div class="avatar abs" role="img" aria-label="Reviewer portrait" style="background:linear-gradient(#e2c2a8,#a56b4d)"></div><p>I just had this procedure done is June and it has literally changed my life! I can make plans now and do them without fear of 'I might have a migraine'.”</p><h5>Barbara</h5><small>One moth ago</small><div class="stars" style="left:255px">★★★★★</div></div>
  <div class="card abs" style="left:991px"><div class="avatar abs" role="img" aria-label="Reviewer portrait" style="background:linear-gradient(#c5d4e2,#7f95aa)"></div><p>Can hardly wait. Had my trial last month, permanent 8/31. Works amazing. I have had migraines for over 50 years and tried so many things.”</p><h5 style="top:132px">Bonnie</h5><small style="top:156px">Two weeks ago</small></div>
</section>

<section class="cta abs">
  <svg width="1017" height="243"><polygon points="0,243 0,0 160,0" fill="#9bcd66"/><polygon points="1017,70 1017,243 860,243" fill="#b2dd7c"/></svg>
  <h2>Need a Help?</h2>
  <p>Contact Talwick Headache Clinics by phone, mail, or through our online form .<br>We welcome your messages, questions, and comments.</p>
  <div class="btn cta-btn abs">Contact Us</div>
</section>

<div class="footer-line abs"></div>
<footer class="site-footer">
  <div class="brand abs">Talwick Headache Clinics</div>
  <div class="footer-about abs">We will always give our customers the best in order to get best experience &nbsp;every time they come.</div>
  <div class="socials abs"><i></i><i></i><i></i><i></i></div>
  <div class="fcol abs" style="left:558px"><h6>Links</h6><div>Home</div><div>Services</div><div>FAQ</div><div>Contact</div></div>
  <div class="fcol abs" style="left:770px"><h6>About</h6><div>News</div><div>Blog</div><div>Career</div><div>Help</div></div>
  <div class="fcol abs" style="left:955px;line-height:17px"><h6>Contact</h6><div style="margin-bottom:10px">Corporate Headquarters<br>2450 Harwell Parkway Suite<br>210 Lornfield, Texas 70412.</div><div style="margin-bottom:14px">(555) 014-2290</div><div>(555) 017-3381</div></div>
  <div class="bottom-bar abs">
    <div class="abs" style="left:0;width:1200px;text-align:center;top:15px">Copyright © 2023 talwickheadache.example</div>
    <div class="abs" style="left:1005px;top:15px">Privacy &nbsp;&nbsp;&nbsp;&nbsp;| &nbsp;&nbsp;&nbsp;&nbsp;Policy</div>
  </div>
</footer>

</body>
</html>
```